Marbrook Jewelers New Website Design

This project is to provide a new design for an existing website. The existing website is marbrookjewelers dot com . I have created a overview document that outlines all the details for the project. I do not need the design to be converted into HTML. I have a team for that already so please don't ask. I have a lot of images .. too many to upload here so they are on my dev server located at pinfernstudio com slash marbrook slash assets

Number of Pages Required

1 page

```html
<!DOCTYPE html>
<html lang="en">
<head>
<meta charset="utf-8">
<title>Marbrook Jewelers</title>
<link rel="stylesheet" href="https://fonts.googleapis.com/css2?family=Lato:ital,wght@0,300;0,400;0,700;1,400&family=Libre+Baskerville&display=swap">
<style>
:root{
  --ink:#1e1e20;
  --dark:#2b2b2d;
  --header:#2a2a2c;
  --band:#b9c7d6;
  --steel:#a9bdd1;
  --steel-text:#dfe8f1;
  --heading-light:#e8e8e8;
  --heading-dark:#3a3a3c;
  --muted:#cfd2d6;
  --card:#f0efeb;
  --star:#e8b93a;
  --footer-head:#a9bdd1;
}
*{margin:0;padding:0;box-sizing:border-box}
html,body{width:1200px;height:2888px;overflow:hidden}
body{position:relative;font-family:"Lato",sans-serif;background:var(--dark);color:#fff}
.abs{position:absolute}
.serif{font-family:"Libre Baskerville",serif}

/* hero */
.hero{left:0;top:0;width:1200px;height:547px;background:radial-gradient(ellipse at 420px 300px,#c9d2dc 0%,#7b8898 25%,#3c4a5e 55%,#1e2a3d 100%)}
.hero-photo{left:330px;top:120px;width:230px;height:340px;border-radius:40%;background:radial-gradient(ellipse,#e6eaee 0%,#a9b3bd 45%,rgba(120,130,140,0) 75%)}
.topbar{left:0;top:0;width:1200px;height:26px;background:linear-gradient(#cfd9e3,#b7c4d1)}
.toplinks{right:235px;top:8px;font-size:9.5px;color:#4a4f57}
.toplinks span{margin:0 5px}
.header{left:0;top:26px;width:1200px;height:61px;background:var(--header)}
.phone{left:233px;top:50px;font-size:10.5px;color:#fff;display:flex;align-items:center;gap:6px}
.hours{right:234px;top:51px;font-size:10px;letter-spacing:1.3px;color:#fff}
.logo{left:553px;top:2px;width:94px;height:94px;border-radius:50%;background:#fff;border:3px solid #e9eef3;display:flex;align-items:center;justify-content:center;font-size:14px;color:#4a6a84;letter-spacing:.5px}
.nav{left:0;top:87px;width:1200px;height:39px;background:rgba(196,210,224,.75)}
.nav span{position:absolute;top:11px;transform:translateX(-50%);font-size:11px;color:#3c4350;white-space:nowrap}
.hero-copy{right:359px;top:250px;text-align:right}
.hero-title{font-size:22px;font-weight:300;letter-spacing:.3px}
.hero-sub{font-size:15px;font-weight:300;margin-top:2px}
.hero-text{font-size:11px;font-weight:300;line-height:15px;margin-top:18px;width:190px;margin-left:auto}
.btn{display:flex;align-items:center;justify-content:center;border-radius:5px;font-size:11px;font-weight:700}
.btn-black{background:#0d0d0e;color:#fff}
.hero-btn{left:679px;top:399px;width:163px;height:33px}
.arrow{top:290px}
.dots{left:559px;top:510px;display:flex;gap:5.5px}
.dots i{width:6px;height:6px;border-radius:50%;background:rgba(255,255,255,.45)}
.dots i:first-child{background:#fff}

/* section headings */
.sec-title{left:0;width:1200px;text-align:center;font-size:19px;letter-spacing:2.5px}
.sec-rule{left:520px;width:161px;height:2px}

/* featured */
.featured{left:0;top:547px;width:1200px;height:877px;background:var(--dark)}
.item{width:257px;height:257px;background:radial-gradient(circle at 50% 42%,#5a5e66 0%,#262a38 30%,#0b0d1c 62%);box-shadow:4px 4px 8px rgba(0,0,0,.45);text-align:center}
.item-name{position:absolute;left:0;width:100%;top:212px;font-size:12px;color:#f2f2f2}
.item-link{position:absolute;left:0;width:100%;top:227px;font-size:9px;color:#c8c8c8}
.browse{left:519px;top:1338px;width:163px;height:34px}

/* about */
.about{left:0;top:1424px;width:1200px;height:511px;background:linear-gradient(90deg,#e9ecf0 0%,#f3f4f6 45%,#eceae8 75%,#e3dcd6 100%)}
.about-deco{left:920px;top:1560px;width:280px;height:200px;background:radial-gradient(ellipse,#d9a48c 0%,rgba(226,190,170,.5) 40%,rgba(236,230,226,0) 72%)}
.photo-frame{left:262px;top:1538px;width:210px;height:237px;background:#d4d6da}
.photo{left:278px;top:1548px;width:212px;height:240px;background:linear-gradient(135deg,#8a8452,#6f7546 40%,#3f4e6b 70%,#b7a07a);box-shadow:2px 2px 6px rgba(0,0,0,.2)}
.about-text{left:520px;top:1548px;width:390px;font-size:12.3px;font-style:italic;letter-spacing:1.1px;line-height:15px;color:#1c1c1e}
.about-text p{margin-bottom:15px}
.more{left:519px;top:1815px;width:163px;height:34px;background:var(--steel);color:var(--steel-text);font-weight:400}

/* testimonials */
.testimonials{left:0;top:1935px;width:1200px;height:360px;background:linear-gradient(#303033,#262628)}
.quote{width:213px;height:143px;border-radius:14px;background:var(--card);color:#555}
.avatar{position:absolute;left:14px;top:13px;width:36px;height:36px;border-radius:50%}
.q-name{position:absolute;left:56px;top:26px;font-size:11.5px;letter-spacing:1.2px;color:#333}
.stars{position:absolute;left:25px;top:54px;font-size:10px;line-height:15.4px;color:var(--star)}
.q-text{position:absolute;left:56px;top:54px;width:150px;font-size:8.6px;line-height:15px;letter-spacing:.7px;color:#777}

/* newsletter */
.newsletter{left:0;top:2295px;width:1200px;height:248px;background:linear-gradient(90deg,#d8dbe0 0%,#e9eaee 30%,#eeeff1 100%)}
.news-sub{left:0;top:2384px;width:1200px;text-align:center;font-size:14px;font-weight:300;color:#444}
.email{left:488px;top:2427px;width:223px;height:23px;border-radius:5px;background:#dadbdd;color:#777;font-size:10px;display:flex;align-items:center;justify-content:center}
.subscribe{left:551px;top:2467px;width:97px;height:24px;background:var(--steel);color:#fff;font-size:8.5px;letter-spacing:.5px;border-radius:5px}

/* footer */
.footer{left:0;top:2543px;width:1200px;height:345px;background:#2b2b2e}
.f-head{font-size:14px;color:var(--footer-head)}
.f-list{font-size:12px;line-height:22.5px;color:#e4e4e4;font-weight:300}
.f-contact{left:232px;font-size:10.5px;display:flex;align-items:center;gap:6px;color:#f0f0f0}
.social{top:2743px;width:17px;height:17px;border-radius:50%;background:#eee}
.social.dim{background:#555}
.f-rule{left:234px;top:2841px;width:731px;height:1px;background:#4a4a4e}
.copyright{left:0;top:2860px;width:1200px;text-align:center;font-size:7.5px;color:#6e6e72}
</style>
</head>
<body>

<!-- hero -->
<div class="abs hero"></div>
<div class="abs hero-photo" role="img" aria-label="Photograph of two silver wedding rings hanging from a chain"></div>
<div class="abs topbar"></div>
<div class="abs toplinks">About us<span>|</span>Contact us</div>
<div class="abs header"></div>
<div class="abs phone">
  <svg width="14" height="14" viewBox="0 0 24 24"><path fill="#fff" d="M6.6 10.8a15.1 15.1 0 0 0 6.6 6.6l2.2-2.2c.3-.3.7-.4 1-.2 1.1.4 2.3.6 3.6.6.6 0 1 .4 1 1V20c0 .6-.4 1-1 1A17 17 0 0 1 3 4c0-.6.4-1 1-1h3.5c.6 0 1 .4 1 1 0 1.3.2 2.5.6 3.6.1.3 0 .7-.2 1z"/></svg>
  <span>: &nbsp;(555)-014-2288</span>
</div>
<div class="abs hours">OPEN FROM 9 AM - 5 PM</div>
<div class="abs logo">Marbrook</div>
<div class="abs nav">
  <span style="left:366px">Company</span>
  <span style="left:472px">Custom jewelry services</span>
  <span style="left:577px">Showcase</span>
  <span style="left:642px">Gallery</span>
  <span style="left:734px">Engraving &amp; Trophies</span>
  <span style="left:832px">Gift Ideas</span>
</div>
<div class="abs hero-copy">
  <div class="hero-title">SAY IT WITH A STONE</div>
  <div class="hero-sub">&amp; Leave her speechless</div>
  <div class="hero-text">Lorem ipsum dolor sit amet, consectetur adipiscing elit, sed do eiusmod tempor incididunt ut labore et dolore magna aliqua. Quis ipsum suspendisse ultrices gravida. Risus</div>
</div>
<div class="abs btn btn-black hero-btn">View Collection</div>
<svg class="abs arrow" style="left:22px" width="18" height="28" viewBox="0 0 18 28"><path d="M14 3 4 14l10 11" fill="none" stroke="#e6e9ee" stroke-width="3"/></svg>
<svg class="abs arrow" style="left:1160px" width="18" height="28" viewBox="0 0 18 28"><path d="M4 3l10 11L4 25" fill="none" stroke="#e6e9ee" stroke-width="3"/></svg>
<div class="abs dots"><i></i><i></i><i></i><i></i><i></i><i></i><i></i></div>

<!-- featured items -->
<div class="abs featured"></div>
<div class="abs sec-title serif" style="top:595px;color:var(--heading-light)">FEATURED ITEMS</div>
<div class="abs sec-rule" style="top:621px;background:#bfc3c8"></div>

<div class="abs item" style="left:297px;top:685px" role="img" aria-label="Photograph of a silver ring set with a dark pearl">
  <div class="item-name">Aria Luna Silver Ring</div><div class="item-link">View collection</div>
</div>
<div class="abs item" style="left:645px;top:685px" role="img" aria-label="Photograph of a gold and diamond bracelet">
  <div class="item-name">Gold &amp; Diamond Bracelet</div><div class="item-link">View collection</div>
</div>
<div class="abs item" style="left:297px;top:1023px" role="img" aria-label="Photograph of an engraved two-tone bracelet">
  <div class="item-name">Silver Engraved Bracelet</div><div class="item-link">View collection</div>
</div>
<div class="abs item" style="left:645px;top:1023px" role="img" aria-label="Photograph of a ring set with a white pearl">
  <div class="item-name">Gold &amp; Pearl Ring</div><div class="item-link">View collection</div>
</div>
<div class="abs btn btn-black browse">Browse All Items</div>

<!-- about -->
<div class="abs about"></div>
<div class="abs about-deco" role="img" aria-label="Photograph of two rose gold rings resting on white lace"></div>
<div class="abs sec-title serif" style="top:1467px;color:var(--heading-dark)">ABOUT US</div>
<div class="abs sec-rule" style="top:1493px;background:#9a9ca0"></div>
<div class="abs photo-frame"></div>
<div class="abs photo" role="img" aria-label="Photograph of the store owners standing outdoors in autumn"></div>
<div class="abs about-text">
  <p>Marbrook Jewelers is an indepdent, family-owned jewelry store located in the heart of downtown Fairhaven. Owner, Daniel Marbrook has been in business since 1990. His wife, Ellen, joined the business in 2010, store manager, Tom, came on board in 2016 and Nora joined the team in 2021.</p>
  <p>Marbrook Jewelers specializes in engagement rings, fashion jewelry and custom designed pieces. Whether you want to create the ring of your dreams or re-create a family heirloom, Marbrook Jewelers is the place to go. Marbrook Jewelers offers on-site repairs and prides themselves on their customer service and competitive prices.</p>
  <p>Marbrook Jewelers offers the selection of the big stores, but with a small town feel and a no-pressure shopping experience.</p>
</div>
<div class="abs btn more">Find out more</div>

<!-- testimonials -->
<div class="abs testimonials"></div>
<div class="abs sec-title serif" style="top:1975px;color:var(--heading-light)">TESTIMONIALS</div>
<div class="abs sec-rule" style="top:2001px;background:#bfc3c8"></div>

<div class="abs quote" style="left:234px;top:2041px">
  <div class="avatar" style="background:linear-gradient(135deg,#c98f78,#7a4a3c)" role="img" aria-label="Customer portrait"></div>
  <div class="q-name serif">CLARA M.</div>
  <div class="stars">★<br>★<br>★<br>★<br>★</div>
  <div class="q-text">Jacob and I had our wedding rings custom-made by Marbrook and it was really amazing. we loved the engraving on them The delivery was quick too.</div>
</div>
<div class="abs quote" style="left:493px;top:2041px">
  <div class="avatar" style="background:linear-gradient(135deg,#9b7a6a,#4a3a34)" role="img" aria-label="Customer portrait"></div>
  <div class="q-name serif">ROSE HALE</div>
  <div class="stars">★<br>★<br>★<br>★<br>★</div>
  <div class="q-text">I had my mom's family heirloom restored by Marbrook and the service was great. They are intended for my newborn twins.</div>
</div>
<div class="abs quote" style="left:752px;top:2041px">
  <div class="avatar" style="background:linear-gradient(135deg,#4a5a7a,#3a2a24)" role="img" aria-label="Customer portrait"></div>
  <div class="q-name serif">OWEN P.</div>
  <div class="stars">★<br>★<br>★<br>★<br>★</div>
  <div class="q-text">I got this custom diamon ring for my fiance from Marbrook and she loved it. We'll be ordering our wedding rings from them soon.</div>
</div>
<svg class="abs" style="left:980px;top:2099px" width="16" height="26" viewBox="0 0 16 26"><path d="M3 3l10 10L3 23" fill="none" stroke="#d8d8d8" stroke-width="3"/></svg>

<!-- newsletter -->
<div class="abs newsletter"></div>
<div class="abs sec-title serif" style="top:2334px;color:var(--heading-dark)">NEWSLETTER</div>
<div class="abs sec-rule" style="top:2360px;left:528px;width:146px;background:#9a9ca0"></div>
<div class="abs news-sub">Stay up to date with our latest trends</div>
<div class="abs email">Email address</div>
<div class="abs btn subscribe">SUBSCRIBE</div>

<!-- footer -->
<div class="abs footer"></div>
<div class="abs f-head" style="left:232px;top:2577px">Contact us</div>
<div class="abs f-contact" style="top:2606px">
  <svg width="14" height="14" viewBox="0 0 24 24"><path fill="#fff" d="M6.6 10.8a15.1 15.1 0 0 0 6.6 6.6l2.2-2.2c.3-.3.7-.4 1-.2 1.1.4 2.3.6 3.6.6.6 0 1 .4 1 1V20c0 .6-.4 1-1 1A17 17 0 0 1 3 4c0-.6.4-1 1-1h3.5c.6 0 1 .4 1 1 0 1.3.2 2.5.6 3.6.1.3 0 .7-.2 1z"/></svg>
  <span>: &nbsp;(555)-014-2288</span>
</div>
<div class="abs f-contact" style="top:2628px">
  <svg width="14" height="14" viewBox="0 0 24 24"><rect x="2" y="5" width="20" height="14" fill="#fff"/><path d="M2 5l10 8 10-8" fill="none" stroke="#2b2b2e" stroke-width="1.6"/></svg>
  <span>: &nbsp;info@marbrookjewelers.com</span>
</div>
<div class="abs f-contact" style="top:2650px">
  <svg width="14" height="16" viewBox="0 0 24 26"><path d="M12 2a7 7 0 0 0-7 7c0 5 7 12 7 12s7-7 7-12a7 7 0 0 0-7-7z" fill="none" stroke="#fff" stroke-width="2"/><circle cx="12" cy="9" r="2.5" fill="#fff"/><ellipse cx="12" cy="23" rx="7" ry="2" fill="none" stroke="#fff" stroke-width="1.5"/></svg>
  <span>: &nbsp;48 Alder Ave, Fairhaven, MN</span>
</div>
<div class="abs f-contact" style="top:2675px">
  <svg width="14" height="14" viewBox="0 0 24 24"><circle cx="12" cy="12" r="11" fill="#fff"/><path d="M12 6v6l4 3" fill="none" stroke="#2b2b2e" stroke-width="2"/></svg>
  <span>: &nbsp;Mondays - Saturdays, 9 AM - 5 PM</span>
</div>
<div class="abs" style="left:233px;top:2716px;font-size:14px;font-weight:300;color:#e4e4e4">Follow us on social media</div>
<div class="abs social" style="left:235px"></div>
<div class="abs social" style="left:265px"></div>
<div class="abs social dim" style="left:296px"></div>
<div class="abs social dim" style="left:326px"></div>

<div class="abs f-head" style="left:528px;top:2578px">Quick links</div>
<div class="abs f-list" style="left:528px;top:2603px">Company<br>Shop online<br>Marbrook showcase<br>Custom design<br>Marbrook watches<br>Gift items<br>Engraving &amp; trophies</div>

<div class="abs f-head" style="left:734px;top:2577px">About us</div>
<div class="abs f-list" style="left:734px;top:2603px">Jewelry serivces &amp; repairs<br>Jewelry eduation<br>Resources<br>More</div>

<div class="abs f-rule"></div>
<div class="abs copyright">COPYRIGHT 2022 WWW.MARBROOKJEWELERS.COM</div>

</body>
</html>
```